Business Card Design Project

I am community manager and social media strategist. I need a double sided business card with company logo and name. Looking for something professional, elegant but also a little bit original.

• - The logo and the colours are the company colours and a required to stay.
- The size should be: 84 x 55 mm (or 3.30 x 2.16)
- The file size should be: 1039 x 697 pixels (300 dpi)
- I'd like rounded corners. :)

Use the following contact information for the card:

Léonie Vardin
Stratégie médias sociaux / community management / édition de sites sociaux
mob. : 0687529103
leonie.vardin@postelune.fr
Twitter. : @lvardin
Skype : vardin.leonie

```html
<!DOCTYPE html>
<html lang="fr">
<head>
<meta charset="utf-8">
<title>Léonie Vardin – carte de visite</title>
<link rel="stylesheet" href="https://fonts.googleapis.com/css2?family=Open+Sans:wght@600;700&display=swap">
<style>
  :root {
    --backdrop: #676767;
    --card-white: #ffffff;
    --brand-blue: #0b5788;
    --contact-blue: #1d5f8f;
    --text-grey: #8c8c8c;
    --back-light: #0aa0e2;
    --back-mid: #0a78bc;
    --back-deep: #0a5590;
    --mark-blue: #1a7fc4;
  }
  * { margin: 0; padding: 0; box-sizing: border-box; }
  html, body {
    width: 1101px;
    height: 1200px;
    overflow: hidden;
    background: var(--backdrop);
    font-family: "Open Sans", Verdana, sans-serif;
  }
  .card {
    position: absolute;
    left: 134px;
    width: 738px;
    height: 481px;
    border-radius: 22px;
    overflow: hidden;
  }
  .card-front { top: 83px; background: var(--card-white); }
  .card-back {
    top: 651px;
    background: linear-gradient(150deg, var(--back-light) 0%, var(--back-mid) 35%, var(--back-deep) 100%);
  }
  .back-pattern {
    position: absolute;
    inset: 0;
    background:
      radial-gradient(ellipse 70% 55% at 18% 12%, rgba(120, 210, 255, 0.35), transparent 70%),
      radial-gradient(ellipse 60% 60% at 80% 95%, rgba(0, 40, 90, 0.35), transparent 70%);
  }
  .brand {
    position: absolute;
    display: flex;
    flex-direction: column;
    align-items: center;
    gap: 14px;
  }
  .brand-dot {
    width: 104px;
    height: 104px;
    border-radius: 50%;
  }
  .brand-name {
    font-weight: 600;
    font-size: 50px;
    letter-spacing: 2px;
    line-height: 1;
  }
  .card-front .brand { left: 55px; top: 60px; width: 202px; }
  .card-front .brand-dot { background: var(--mark-blue); }
  .card-front .brand-name { color: var(--brand-blue); }
  .card-back .brand { left: 210px; top: 280px; width: 180px; gap: 10px; }
  .card-back .brand-dot { width: 90px; height: 90px; background: #ffffff; }
  .card-back .brand-name { color: #ffffff; font-size: 44px; }

  .contact {
    position: absolute;
    right: 63px;
    top: 55px;
    text-align: right;
    font-weight: 700;
    font-size: 21px;
    line-height: 24px;
    list-style: none;
  }
  .contact li { display: flex; justify-content: flex-end; align-items: center; gap: 8px; }
  .contact .mobile { color: var(--contact-blue); }
  .contact .email { color: var(--brand-blue); }
  .contact .social { color: var(--text-grey); }
  .social-mark {
    width: 20px;
    height: 20px;
    border-radius: 4px;
    background: var(--mark-blue);
  }
  .holder-name {
    position: absolute;
    left: 56px;
    top: 302px;
    color: var(--brand-blue);
    font-weight: 700;
    font-size: 27px;
  }
  .holder-role {
    position: absolute;
    left: 56px;
    top: 360px;
    width: 560px;
    color: var(--text-grey);
    font-weight: 700;
    font-size: 21px;
    line-height: 27px;
  }
</style>
</head>
<body>
  <section class="card card-front">
    <div class="brand">
      <span class="brand-dot"></span>
      <span class="brand-name">VENTARA</span>
    </div>
    <ul class="contact">
      <li class="mobile">mob. : 0687529103</li>
      <li class="email">leonie.vardin@postelune.fr</li>
      <li class="social"><span class="social-mark"></span>@lvardin</li>
      <li class="social"><span class="social-mark"></span>vardin.leonie</li>
    </ul>
    <h1 class="holder-name">Léonie Vardin</h1>
    <p class="holder-role">Stratégie médias sociaux / community management / édition de sites sociaux</p>
  </section>

  <section class="card card-back">
    <div class="back-pattern" role="img" aria-label="Large soft blue swoosh decoration"></div>
    <div class="brand">
      <span class="brand-dot"></span>
      <span class="brand-name">VENTARA</span>
    </div>
  </section>
</body>
</html>
```